Doctor in Veterinary Medecine/ veterinarian

I am a vet and would like a buisness card which is simple yet elegant and professional.
My aim is to help as much animals as I can. My main field of expertise are dogs and cats. I would like the card to reflect a "family doctor" feeling.
It should not be the traditional picture of a paw or a dog but yet it should have a sign of a pet on it. I would like to have my name Lina Haddour as well as my profession D.V.M and my number.

Target Market(s)

Lebanese population who have pets

Industry/Entity Type

Doctor

Contact Information for Business Card

Should contain my profession " D.V.M", my full name "Lina Haddour" and my number "0096171552934"

Requirements
Must have
• A certain picture depicting my profession
Nice to have
• Some sort of picture related to pets and animals
Should not have
• A picture of a paw or a dog. I need something more creative

```html
<!DOCTYPE html>
<html lang="en">
<head>
<meta charset="utf-8">
<title>Lina Haddour D.V.M — Business Card</title>
<link rel="stylesheet" href="https://fonts.googleapis.com/css2?family=Marcellus&display=swap">
<style>
  :root {
    --backdrop: #ecebee;
    --card: #ffffff;
    --coral: #e2514f;
    --blush: #fbe6e8;
    --blush-deep: #f7d9dc;
    --ink: #4f4f52;
  }
  html, body {
    margin: 0;
    padding: 0;
    width: 1200px;
    height: 1000px;
    overflow: hidden;
    background: var(--backdrop);
  }
  .canvas {
    position: relative;
    width: 1200px;
    height: 1000px;
    display: flex;
    align-items: center;
    justify-content: center;
  }
  .business-card {
    position: relative;
    width: 530px;
    height: 900px;
    background: var(--card);
    box-shadow: 0 6px 24px rgba(0, 0, 0, 0.12);
    overflow: hidden;
  }
  .pet-backdrop {
    position: absolute;
    left: 0;
    right: 0;
    top: 360px;
    bottom: 0;
    background:
      radial-gradient(ellipse 60% 45% at 62% 40%, rgba(246, 211, 216, 0.75) 0%, rgba(246, 211, 216, 0) 100%),
      radial-gradient(ellipse 80% 55% at 40% 75%, rgba(249, 222, 225, 0.8) 0%, rgba(249, 222, 225, 0) 100%),
      linear-gradient(180deg, rgba(251, 230, 232, 0) 0%, rgba(251, 230, 232, 0.55) 30%, var(--blush) 60%, var(--blush-deep) 100%);
  }
  .pet-mark {
    position: absolute;
    left: 155px;
    top: 110px;
    width: 230px;
    height: 170px;
    border-radius: 10px;
    background: linear-gradient(180deg, var(--coral) 0%, #e86563 100%);
  }
  .mark-rule {
    position: absolute;
    left: 135px;
    top: 292px;
    width: 270px;
    height: 3px;
    background: var(--coral);
  }
  .contact {
    position: absolute;
    z-index: 1;
    left: 0;
    right: 0;
    top: 312px;
    text-align: center;
    font-family: "Marcellus", "Optima", serif;
    color: var(--ink);
    font-size: 29px;
    line-height: 1.28;
    letter-spacing: 0.5px;
  }
  .contact p { margin: 0; }
  .contact .name { text-transform: uppercase; }
</style>
</head>
<body>
  <main class="canvas">
    <article class="business-card">
      <div class="pet-backdrop" role="img" aria-label="Faint large silhouettes of a dog and a cat"></div>
      <div class="pet-mark" role="img" aria-label="Coral silhouette of a dog with a cat standing inside it"></div>
      <div class="mark-rule"></div>
      <section class="contact">
        <p class="name">Lina Haddour</p>
        <p class="title">D.V.M</p>
        <p class="phone">0096171552934</p>
      </section>
    </article>
  </main>
</body>
</html>
```